Business Card Design Project - IT Company

Kestrafield Information Technology Solutions
We are an Information Technology Company. We provide computer services to commercial companies. We would like a new card full color front and back with bleeding edge.
We have a logo that you can use or if you want to come up with a new logo that is fine too.
Our colors are mostly Maroon and black but be creative.
Sample Information
Brent R Okafor
4812 W Saguaro Ridge Drive
Suite 600
Phoenix, AZ 85016
O: 602.914.2037
C: 602.468.1290
24/7: 888.914.2037
bokafor@kestrafield.example
www.kestrafield.example
Target Market(s)
Business of all sizes
Industry/Entity Type
Computer
Requirements
Must have
- Bleeding edge
full color on both sides

```html
<!DOCTYPE html>
<html lang="en">
<head>
<meta charset="utf-8">
<title>Kestrafield Business Card – Front and Back</title>
<link rel="stylesheet" href="https://fonts.googleapis.com/css2?family=Arimo:wght@400;700&family=Tinos&display=swap">
<style>
  :root {
    --page: #262626;
    --card: #0c0c0c;
    --card-texture-a: #141414;
    --card-texture-b: #0a0a0a;
    --text-grey: #8c8c8c;
    --accent-red: #c8102e;
  }
  * { margin: 0; padding: 0; box-sizing: border-box; }
  html, body {
    width: 1200px;
    height: 898px;
    overflow: hidden;
    background: var(--page);
  }
  .canvas {
    position: relative;
    width: 1200px;
    height: 898px;
    background: var(--page);
  }
  .card {
    position: absolute;
    width: 680px;
    height: 396px;
    background: var(--card);
    font-family: "Arimo", Arial, sans-serif;
    color: var(--text-grey);
    overflow: hidden;
  }
  .card--front { left: 53px; top: 40px; }
  .card--back  { left: 398px; top: 477px; width: 675px; }
  .card-texture {
    position: absolute;
    inset: 0;
    background: linear-gradient(160deg, var(--card-texture-a), var(--card-texture-b));
  }
  .brand {
    position: absolute;
    display: flex;
    flex-direction: column;
    align-items: center;
  }
  .card--front .brand { left: 160px; top: 160px; width: 360px; }
  .card--back  .brand { left: 10px;  top: 133px; width: 340px; }
  .brand-row {
    display: flex;
    align-items: center;
    gap: 12px;
  }
  .brand-mark {
    width: 26px;
    height: 26px;
    background: var(--accent-red);
  }
  .brand-name {
    font-family: "Arimo", Arial, sans-serif;
    font-weight: 400;
    font-size: 46px;
    line-height: 1;
    letter-spacing: 0.5px;
    color: var(--text-grey);
  }
  .brand-tagline {
    margin-top: 10px;
    font-family: "Tinos", "Times New Roman", serif;
    font-size: 14px;
    color: var(--text-grey);
  }
  .website {
    position: absolute;
    font-weight: 700;
    font-size: 21px;
    color: var(--text-grey);
  }
  .card--front .website { right: 16px; bottom: 18px; }
  .card--back  .website { left: 30px; bottom: 18px; font-size: 18px; }
  .contact {
    position: absolute;
    left: 370px;
    top: 60px;
    width: 240px;
    text-align: center;
    font-weight: 700;
    font-size: 14px;
  }
  .contact-name { font-size: 18px; margin-bottom: 30px; }
  .contact-line { margin-bottom: 30px; }
  .address {
    position: absolute;
    right: 14px;
    bottom: 20px;
    font-weight: 700;
    font-size: 11.5px;
  }
</style>
</head>
<body>
<main class="canvas">

  <section class="card card--front" aria-label="Card front">
    <div class="card-texture" role="img" aria-label="Faint binary-digit texture across the card"></div>
    <div class="brand">
      <div class="brand-row">
        <span class="brand-mark"></span>
        <span class="brand-name">KESTRAFIELD</span>
      </div>
      <p class="brand-tagline">Information Technology Solutions</p>
    </div>
    <p class="website">www.kestrafield.example</p>
  </section>

  <section class="card card--back" aria-label="Card back">
    <div class="card-texture" role="img" aria-label="Faint binary-digit texture across the card"></div>
    <div class="brand">
      <div class="brand-row">
        <span class="brand-mark"></span>
        <span class="brand-name" style="font-size:40px">KESTRAFIELD</span>
      </div>
      <p class="brand-tagline">Information Technology Solutions</p>
    </div>
    <div class="contact">
      <p class="contact-name">Brent R Okafor</p>
      <p class="contact-line">O: 602.914.2037</p>
      <p class="contact-line">C: 602.468.1290</p>
      <p class="contact-line">24/7: 888.914.2037</p>
      <p class="contact-line">Email: bokafor@kestrafield.example</p>
    </div>
    <p class="website">www.kestrafield.example</p>
    <p class="address">4812 W Saguaro Ridge Drive Suite 600 Phoenix, AZ 85016</p>
  </section>

</main>
</body>
</html>
```